Design a business card & stationary for a mortgage company

We are looking for a good looking business card design for our mortgage company that includes our logo. We received a free design as part of our logo project but we don't love it. The company is called "Birchfield Mortgage Company" so we like waves and lighthouses. The logo should be included. We have a version in both vertical and horizontal that we have provided.

Industry/Entity Type

Finance

Contact Information for Business Card

This should include our new logo file

Requirements
Must have
• 3. The details you'd like on the card - name, title, phone, email, website, address, social media handles etc.
1. Dennis Marlow
Vice President
614-390-2751
Fax 877-402-6158
dmarlow@birchfieldmortgage.example
NMLS 47192 - Company NMLS 62304
18 Elm Ave
Harwick Cove, DE 08512

```html
<!DOCTYPE html>
<html lang="en">
<head>
<meta charset="utf-8">
<title>Birchfield Mortgage Company – Stationery</title>
<link href="https://fonts.googleapis.com/css2?family=Lato:wght@400;700;900&family=Roboto+Condensed:wght@300&display=swap" rel="stylesheet">
<style>
  :root{
    --bg:#d9e4ef;
    --navy:#135a93;
    --sky:#0d96dc;
    --ink:#1a5d99;
    --body:#555a60;
    --paper:#ffffff;
  }
  *{box-sizing:border-box;margin:0;padding:0}
  html,body{width:1200px;height:831px;overflow:hidden;background:var(--bg)}
  body{position:relative;font-family:"Lato",sans-serif;color:var(--ink)}
  .sheet{position:absolute;background:var(--paper);box-shadow:0 3px 10px rgba(40,60,90,.28);overflow:hidden}
  .swoosh{position:absolute;left:0;bottom:0;width:100%;display:block}
  .wordmark{font-family:"Lato",sans-serif;font-weight:900;color:var(--navy);line-height:1.05;display:flex;align-items:center;gap:.35em}
  .wordmark .dot{width:.6em;height:.6em;border-radius:50%;background:currentColor;flex:none}
  .icon{width:1em;height:1em;display:inline-block;vertical-align:-.12em;fill:var(--sky)}

  /* letterhead */
  .letterhead{left:117px;top:111px;width:430px;height:609px}
  .letterhead .wordmark{position:absolute;left:39px;top:40px;width:160px;font-size:16px}
  .letterhead .contact{position:absolute;right:42px;top:30px;text-align:right;font-size:7.8px;line-height:9.2px}
  .letterhead .contact .gap{height:3px}
  .letterhead .contact .icon{margin-left:5px}
  .letter{position:absolute;left:39px;top:200px;width:349px;font-family:"Roboto Condensed",sans-serif;font-weight:300;color:var(--body);font-size:9.7px;line-height:15px;text-align:justify}
  .letter p{margin-bottom:15px}
  .letter .greeting{margin-bottom:13px}
  .letter .closing{margin-top:36px;margin-bottom:6px}
  .signature{width:36px;height:24px;background:linear-gradient(90deg,#dfe9f3,#c6d7e8);border-radius:3px}

  /* business card front */
  .card-front{left:635px;top:112px;width:183px;height:104px}
  .card-front .wordmark{position:absolute;left:10px;top:36px;width:74px;font-size:8.5px}
  .card-front .divider{position:absolute;left:89px;top:27px;width:1px;height:51px;background:var(--navy)}
  .card-front .details{position:absolute;left:100px;right:4px;top:25px;font-size:3.5px;line-height:4.7px;white-space:nowrap}
  .card-front .name{font-weight:900;font-size:7.4px;line-height:8px;color:var(--navy)}
  .card-front .title{color:var(--sky);font-size:4.8px;line-height:6px;margin-bottom:2.5px}
  .card-front .gap{height:2px}
  .card-front .icon{margin-right:3px}

  /* business card back */
  .card-back{left:904px;top:111px;width:183px;height:104px;background:var(--navy)}
  .card-back .wordmark{position:absolute;left:0;right:0;top:44px;justify-content:center;color:#fff;font-size:11px}

  /* envelope back */
  .envelope-back{left:635px;top:248px;width:452px;height:225px}
  .envelope-back .flap{position:absolute;left:0;top:0;width:452px;height:66px;display:block}
  .envelope-back .wordmark{position:absolute;left:0;right:0;top:24px;justify-content:center;color:#fff;font-size:10px}

  /* envelope front */
  .envelope-front{left:635px;top:494px;width:452px;height:226px}
  .envelope-front .wordmark{position:absolute;left:39px;top:38px;width:160px;font-size:16px}
  .envelope-front .contact{position:absolute;left:40px;top:146px;font-size:6.3px;line-height:7.1px}
  .envelope-front .gap{height:4px}
  .envelope-front .icon{margin-right:4px}
</style>
</head>
<body>

<svg width="0" height="0" style="position:absolute" aria-hidden="true">
  <defs>
    <symbol id="i-phone" viewBox="0 0 10 10"><path d="M2.2 1 3.8 1 4.4 3.2 3.3 4a5.5 5.5 0 0 0 2.7 2.7L6.8 5.6 9 6.2v1.6C9 8.5 8.5 9 7.8 9 4.1 9 1 5.9 1 2.2 1 1.5 1.5 1 2.2 1Z"/></symbol>
    <symbol id="i-fax" viewBox="0 0 10 10"><rect x="3" y="1" width="4" height="2.5"/><rect x="1" y="3.5" width="8" height="4" rx="1"/><rect x="3" y="6.5" width="4" height="2.5"/></symbol>
    <symbol id="i-mail" viewBox="0 0 10 10"><rect x="1" y="2.5" width="8" height="5.5" rx=".6"/></symbol>
    <symbol id="i-web" viewBox="0 0 10 10"><circle cx="5" cy="5" r="4"/></symbol>
  </defs>
</svg>

<!-- Letterhead -->
<section class="sheet letterhead">
  <div class="wordmark"><span class="dot"></span><span>Birchfield Mortgage Company</span></div>
  <address class="contact" style="font-style:normal">
    <div>NMLS 47192 - Company NMLS 62304</div>
    <div>18 Elm Ave</div>
    <div>Harwick Cove, DE 08512</div>
    <div class="gap"></div>
    <div>614-390-2751<svg class="icon"><use href="#i-phone"/></svg></div>
    <div>877-402-6158<svg class="icon"><use href="#i-fax"/></svg></div>
    <div>dmarlow@birchfieldmortgage.example<svg class="icon"><use href="#i-mail"/></svg></div>
    <div>www.birchfieldmortgage.example<svg class="icon"><use href="#i-web"/></svg></div>
  </address>
  <div class="letter">
    <p class="greeting">Dear Sir/Mam,</p>
    <p>Contrary to popular belief, Lorem Ipsum is not simply random text. It has roots in a piece of classical Latin literature from 45 BC, making it over 2000 years old. Howard Pellman, a Latin professor at Ashgrove College in Virginia, looked up one of the more obscure Latin words, consectetur.</p>
    <p>Lorem Ipsum comes from sections 1.10.32 and 1.10.33 of "de Finibus Bonorum et Malorum" (The Extremes of Good and Evil) by Lucius Avernus, written in 45 BC. This book is a treatise on the theory of ethics, very popular during the Renaissance. The first line of Lorem Ipsum.</p>
    <p>The standard chunk of Lorem Ipsum used since the 1500s is reproduced below for those interested. Sections 1.10.32 and 1.10.33 from "de Finibus Bonorum et Malorum" by Lucius Avernus are also reproduced in their exact original.</p>
    <p>The standard chunk of Lorem Ipsum used since the 1500s is reproduced below for those interested.</p>
    <p class="closing">Best Regards</p>
    <div class="signature" role="img" aria-label="Handwritten signature"></div>
  </div>
  <svg class="swoosh" viewBox="0 0 430 30" height="30" preserveAspectRatio="none" aria-hidden="true">
    <path d="M118 30C200 12 300 1 385 1L430 4V30Z" fill="var(--sky)"/>
    <path d="M165 30C245 14 335 5 430 6V30Z" fill="#fff"/>
    <path d="M172 30C252 15 342 7 430 9V30Z" fill="var(--navy)"/>
  </svg>
</section>

<!-- Business card front -->
<section class="sheet card-front">
  <div class="wordmark"><span>Birchfield Mortgage Company</span></div>
  <div class="divider"></div>
  <div class="details">
    <div class="name">DENNIS MARLOW</div>
    <div class="title">Vice President</div>
    <div>NMLS 47192 - Company NMLS 62304</div>
    <div>18 Elm Ave</div>
    <div>Harwick Cove, DE 08512</div>
    <div class="gap"></div>
    <div><svg class="icon"><use href="#i-phone"/></svg>614-390-2751</div>
    <div><svg class="icon"><use href="#i-fax"/></svg>877-402-6158</div>
    <div><svg class="icon"><use href="#i-mail"/></svg>dmarlow@birchfieldmortgage.example</div>
    <div><svg class="icon"><use href="#i-web"/></svg>www.birchfieldmortgage.example</div>
  </div>
  <svg class="swoosh" viewBox="0 0 183 12" height="12" preserveAspectRatio="none" aria-hidden="true">
    <path d="M58 12C95 5 130 1 160 1L183 2V12Z" fill="var(--sky)"/>
    <path d="M76 12C110 6 145 3 183 3V12Z" fill="#fff"/>
    <path d="M79 12C113 7 148 4 183 4V12Z" fill="var(--navy)"/>
  </svg>
</section>

<!-- Business card back -->
<section class="sheet card-back">
  <div class="wordmark"><span>Birchfield Mortgage Company</span></div>
</section>

<!-- Envelope back -->
<section class="sheet envelope-back">
  <svg class="flap" viewBox="0 0 452 66" aria-hidden="true">
    <path d="M0 0H452L447 40Q445 66 418 66H34Q7 66 5 40Z" fill="var(--navy)"/>
  </svg>
  <div class="wordmark"><span>Birchfield Mortgage Company</span></div>
</section>

<!-- Envelope front -->
<section class="sheet envelope-front">
  <div class="wordmark"><span class="dot"></span><span>Birchfield Mortgage Company</span></div>
  <address class="contact" style="font-style:normal">
    <div>NMLS 47192 - Company NMLS 62304</div>
    <div>18 Elm Ave</div>
    <div>Harwick Cove, DE 08512</div>
    <div class="gap"></div>
    <div><svg class="icon"><use href="#i-phone"/></svg>614-390-2751</div>
    <div><svg class="icon"><use href="#i-fax"/></svg>877-402-6158</div>
    <div><svg class="icon"><use href="#i-mail"/></svg>dmarlow@birchfieldmortgage.example</div>
    <div><svg class="icon"><use href="#i-web"/></svg>www.birchfieldmortgage.example</div>
  </address>
  <svg class="swoosh" viewBox="0 0 452 28" height="28" preserveAspectRatio="none" aria-hidden="true">
    <path d="M138 28C215 11 305 1 400 1L452 4V28Z" fill="var(--sky)"/>
    <path d="M187 28C265 13 355 5 452 6V28Z" fill="#fff"/>
    <path d="M194 28C272 14 362 7 452 9V28Z" fill="var(--navy)"/>
  </svg>
</section>

</body>
</html>
```